Website design for luxury private hair salon

I'm looking for someone to use my Logo and build me a website for my webpage www.lunetresses.com.au (You can have a look at it as it has every detail I need included on it already), however I want a fresh new appearance and it to look and feel super stylish.

I am thinking colours in black, with silver or white, beautiful hair images like the ones you'll see on the current webpage - the price list as per what you already see.

I will include a copy of my biz card on here, so you can see the feel of the card, and design a website with a similar feel. It is matt black with a foil silver.

Modern, but classic and fresh. I will also need you to be able to publish it to my URL for me as I have no idea how to do this. I need it up and running pronto!

The website will need to be able to be read clearly on all devices incluing smart phones and ipads. The URL is currently registered and hosted by Nimbo Vault

Thinking a Home Page - large logo etc and write up on who and what we offer
Services/Price List page - as per the price list on my current webpage
Contact Page - with a built in contact form.

Target Market(s)

Middle aged, fashionable, stylish women and men who enjoy luxury hair care and styling in an upmarket location.

Industry/Entity Type

Hair And Beauty

Number of Pages Required

3 page

Font styles to use
Other font styles liked:
• see my images for my current logo

Colors
000000
b2b2b2
a54499

Requirements
Must have
• Style
• Fast turnaround
• Be viewable on all devices, PC, ipads, smart phones
• Designer able to upload it so its a running website for me to my URL
Nice to have
• Just a really feminine, stylish website which is easy to read and shows some beautiful images of perfect hair
Should not have
• Browns, reds or orange colours.

```html
<!DOCTYPE html>
<html lang="en">
<head>
<meta charset="utf-8">
<title>Lune Tresses – Home Page Concept</title>
<link rel="stylesheet" href="https://fonts.googleapis.com/css2?family=Roboto+Condensed:wght@300&family=Libre+Baskerville&family=EB+Garamond:wght@400&family=Cinzel:wght@400&family=Great+Vibes&display=swap">
<style>
  :root {
    --stage: #474546;
    --stage-dark: #3a3839;
    --note: #ffffff;
    --header: #000000;
    --gold: #c9a20b;
    --band: #d8b000;
    --magenta: #b3287f;
    --nav-white: #ffffff;
    --dot-grey: #b2b2b2;
    --hero-cool: #5a6069;
    --hero-mid: #8a8e96;
    --hero-warm: #c9a682;
  }
  * { box-sizing: border-box; margin: 0; padding: 0; }
  html, body { width: 1200px; height: 1200px; overflow: hidden; }
  body {
    position: relative;
    background: radial-gradient(ellipse at 50% 40%, var(--stage) 0%, var(--stage-dark) 100%);
    font-family: "Libre Baskerville", Georgia, serif;
  }
  .presentation-note {
    position: absolute; left: 37px; top: 38px;
    font-family: "Roboto Condensed", "Arial Narrow", sans-serif;
    font-weight: 300; font-size: 16px; line-height: 19px;
    color: var(--note);
  }
  .presentation-note p + p { margin-top: 20px; }

  .site { position: absolute; left: 37px; top: 238px; width: 1126px; height: 751px; overflow: hidden; }
  .site-header { position: relative; height: 122px; background: var(--header); }
  .brand {
    position: absolute; left: 52px; top: 36px;
    font-size: 38px; color: var(--gold); letter-spacing: 0.5px;
  }
  .main-nav {
    position: absolute; top: 84px; left: 641px;
    display: flex; align-items: center;
    font-family: "Cinzel", "Times New Roman", serif; font-size: 15px;
  }
  .main-nav a { text-decoration: none; color: var(--magenta); }
  .main-nav a.is-current { color: var(--nav-white); }
  .nav-sep { width: 5px; height: 5px; border-radius: 50%; background: var(--magenta); margin: 0 44px 0 42px; }
  .gold-band { height: 10px; background: var(--band); }

  .hero { position: relative; height: 619px; }
  .hero-photo {
    position: absolute; inset: 0;
    background:
      radial-gradient(ellipse 45% 70% at 72% 45%, var(--hero-warm) 0%, rgba(201,166,130,0.55) 45%, rgba(201,166,130,0) 80%),
      linear-gradient(100deg, var(--hero-cool) 0%, var(--hero-mid) 45%, var(--hero-cool) 100%);
  }
  .hero-quote {
    position: absolute; left: 53px; top: 62px;
    font-family: "EB Garamond", Georgia, serif;
    color: #ffffff; font-size: 20px; line-height: 23px;
  }
  .hero-quote span { display: block; white-space: nowrap; }
  .hero-signature {
    position: absolute; left: 266px; top: 210px;
    font-family: "Great Vibes", cursive; font-size: 28px; line-height: 32px; color: #ffffff;
  }
  .slider-arrow { position: absolute; top: 276px; }
  .slider-arrow.prev { left: 24px; }
  .slider-arrow.next { right: 22px; }
  .slider-dots { position: absolute; left: 498px; top: 566px; display: flex; gap: 9px; }
  .slider-dots span {
    width: 23px; height: 23px; border-radius: 50%;
    background: var(--dot-grey); border: 3px solid #ffffff;
  }
  .slider-dots span.is-active { background: var(--magenta); }
</style>
</head>
<body>
  <div class="presentation-note">
    <p>All Pictures Can be replaced at the psd final layered file also all text</p>
    <p>Please note that we reduced the size of Lune logo to provide the idea<br>of scrolling 5 pictures showing the services and home page information</p>
  </div>

  <div class="site">
    <header class="site-header">
      <div class="brand">Lune Tresses</div>
      <nav class="main-nav">
        <a class="is-current" href="#">HOME</a>
        <span class="nav-sep"></span>
        <a href="#">PRICE LIST</a>
        <span class="nav-sep"></span>
        <a href="#">CONTCT US</a>
      </nav>
    </header>
    <div class="gold-band"></div>

    <section class="hero">
      <div class="hero-photo" role="img" aria-label="Portrait of a model with long, voluminous blonde curls against a cool grey studio backdrop"></div>
      <blockquote class="hero-quote">
        <span>"We pride ourselves on being able to offer a</span>
        <span>private salon experience to our clients in the</span>
        <span>exclusive suburb of Ashbury Vale, where your</span>
        <span>hair design and colouring needs will be met</span>
        <span>with years of experience and current</span>
        <span>industry training and knowledge".</span>
      </blockquote>
      <div class="hero-signature">The Lune Team</div>

      <svg class="slider-arrow prev" width="34" height="40" viewBox="0 0 34 40" aria-label="Previous slide">
        <polyline points="31,3 4,20 31,37" fill="none" stroke="#ffffff" stroke-width="3"/>
      </svg>
      <svg class="slider-arrow next" width="34" height="40" viewBox="0 0 34 40" aria-label="Next slide">
        <polyline points="3,3 30,20 3,37" fill="none" stroke="#ffffff" stroke-width="3"/>
      </svg>

      <div class="slider-dots">
        <span class="is-active"></span><span></span><span></span><span></span><span></span>
      </div>
    </section>
  </div>
</body>
</html>
```